Wanted: A Simple yet Awesome Blog Hero Image

We need a hero image (blog graphic header) to replace our existing one: https://www.brantwellsupply.com//blog/soil-classification-foundation-and-pavement-design-starts-here
Want something to reflect what the blog article is about and is a reflection of the title.

Note: we are not in love with any of our hero graphics

Industry/Entity Type

Construction

Colors

Designer to choose colors to be used in the design.

Requirements
Must have
• Width must be 715px
• Height must not exceed 400px
• Content on graphic should be: Soil Classification: Foundation and Pavement Design Starts Here
Nice to have
• a product shown that is mentioned in the blog
Should not have
• a product with a Carraway logo

```html
<!DOCTYPE html>
<html lang="en">
<head>
<meta charset="utf-8">
<title>Soil Classification: Foundation and Pavement Design Starts Here</title>
<link rel="stylesheet" href="https://fonts.googleapis.com/css2?family=Oswald:wght@300;400;700&display=swap">
<style>
  :root {
    --charcoal: #262425;
    --brand-blue: #1a6ec2;
    --deep-blue: #0f5aa6;
    --white: #ffffff;
    --sky: #5d8fc4;
    --hill: #a6865f;
    --asphalt: #6f6f6f;
  }
  html, body {
    margin: 0;
    padding: 0;
    overflow: hidden;
    background: var(--charcoal);
  }
  .hero {
    position: relative;
    width: 1200px;
    height: 671px;
    overflow: hidden;
    background: var(--charcoal);
    font-family: "Oswald", sans-serif;
  }
  .hero-shapes {
    position: absolute;
    inset: 0;
    width: 1200px;
    height: 671px;
  }
  .hero-title {
    position: absolute;
    top: 92px;
    left: 166px;
    margin: 0;
    font-weight: 700;
    font-size: 100px;
    line-height: 1;
    letter-spacing: 1px;
    color: var(--white);
    white-space: nowrap;
  }
  .hero-title .accent { color: var(--brand-blue); }
  .hero-subtitle {
    position: absolute;
    margin: 0;
    top: 278px;
    left: 0;
    width: 1200px;
    font-weight: 400;
    font-size: 60px;
    line-height: 92px;
    color: var(--white);
    text-transform: uppercase;
  }
  .hero-subtitle .line {
    position: absolute;
    white-space: nowrap;
  }
  .hero-subtitle .line-1 { left: 146px; top: 0; letter-spacing: 2px; }
  .hero-subtitle .line-2 { left: 108px; top: 92px; letter-spacing: 2px; }
  .hero-subtitle .line-3 { left: 82px; top: 184px; letter-spacing: 9px; }
  .hero-subtitle .accent { color: var(--brand-blue); }
</style>
</head>
<body>
<main class="hero">
  <svg class="hero-shapes" viewBox="0 0 1200 671" aria-hidden="false">
    <defs>
      <linearGradient id="road-scene" x1="0" y1="0" x2="0" y2="1">
        <stop offset="0" stop-color="#4f86c6"/>
        <stop offset="0.22" stop-color="#9bb8d6"/>
        <stop offset="0.3" stop-color="#a6865f"/>
        <stop offset="0.45" stop-color="#8c7a5c"/>
        <stop offset="0.55" stop-color="#7d7d7d"/>
        <stop offset="1" stop-color="#5e5e5e"/>
      </linearGradient>
    </defs>
    <!-- blue chevron band -->
    <polygon class="chevron-band" points="758,0 1200,0 1200,671 848,671 630,320" fill="var(--brand-blue)"/>
    <!-- dark gap -->
    <polygon class="chevron-gap" points="790,0 1200,0 1200,640 866,640 664,320" fill="var(--charcoal)"/>
    <!-- photo area -->
    <polygon class="hero-photo" role="img" aria-label="Photo of an empty paved highway running through dry hills under a blue sky"
      points="806,0 1200,0 1200,620 888,620 690,320" fill="url(#road-scene)"/>
    <!-- bottom band and stripes -->
    <rect class="base-band" x="720" y="640" width="480" height="31" fill="var(--deep-blue)"/>
    <polygon class="base-stripe" points="628,671 660,640 700,640 668,671" fill="var(--brand-blue)"/>
    <polygon class="base-stripe" points="680,671 712,640 740,640 708,671" fill="var(--white)"/>
    <polygon class="base-stripe" points="1030,671 1062,640 1100,640 1068,671" fill="var(--white)"/>
    <polygon class="base-stripe" points="1110,671 1142,640 1200,640 1200,671" fill="var(--brand-blue)"/>
  </svg>

  <h1 class="hero-title"><span class="accent">SOIL</span> CLASSIFICATION</h1>
  <p class="hero-subtitle">
    <span class="line line-1"><span class="accent">Foundation</span> and</span>
    <span class="line line-2"><span class="accent">Pavement</span> Design</span>
    <span class="line line-3">Starts <span class="accent">Here</span></span>
  </p>
</main>
</body>
</html>
```